Velmora Roasters

Full Shopify site .
About page

Merch page
Tshirts, hats, mugs

Coffee page
-sections
Single origin
Tamblin series
Quillet series
Decaf

VelmoraQ page
Cold brew
Coffee liquor
Absinthe Coffee

```html
<!DOCTYPE html>
<html lang="en">
<head>
<meta charset="utf-8">
<title>Velmora Roasters</title>
<link href="https://fonts.googleapis.com/css2?family=Poppins:wght@300;400;500;600;700&display=swap" rel="stylesheet">
<style>
:root{
  --red:#e8372b;
  --ink:#111111;
  --text:#444444;
  --pink:#fde9e9;
  --footer:#1c1c1c;
  --white:#ffffff;
  --card-line:#f3c7c4;
  --bean-tone:rgba(106,67,44,.18);
}
*{box-sizing:border-box;margin:0;padding:0}
html,body{width:1200px;height:4653px;overflow:hidden}
body{font-family:'Poppins',sans-serif;color:var(--ink);background:var(--white);position:relative}
.abs{position:absolute}
.btn{position:absolute;background:var(--red);color:var(--white);font-size:13px;font-weight:500;display:flex;align-items:center;justify-content:center}
.photo{position:absolute}
.bean-area{position:absolute;background:var(--bean-tone)}
.topbar{left:0;top:0;width:1200px;height:36px;background:#000;color:#fff;font-size:11px;font-weight:500;display:flex;align-items:center;justify-content:center;letter-spacing:.3px}
.header{left:0;top:36px;width:1200px;height:87px;background:#fff;border-bottom:1px solid #eee}
.brand{left:160px;top:30px;display:flex;align-items:center;gap:8px;font-size:15px;font-weight:700;color:var(--ink)}
.brand-dot{width:22px;height:22px;border-radius:50%;background:var(--red)}
.nav a{position:absolute;top:38px;font-size:12px;color:#222;text-decoration:none;transform:translateX(-50%)}
.icon{position:absolute;top:32px}
.hero{left:0;top:123px;width:1200px;height:439px;background:radial-gradient(ellipse at 50% 40%,#6b4a34 0%,#3a2418 55%,#1c110b 100%)}
.hero h1{position:absolute;width:1200px;text-align:center;color:#fff;font-weight:500;line-height:1}
.hero p{position:absolute;top:254px;width:1200px;text-align:center;color:#fff;font-size:15px}
.section-title{position:absolute;width:1200px;text-align:center;font-weight:600;font-size:31px}
.about-text{left:264px;top:673px;width:672px;text-align:center;font-size:12.5px;line-height:18px;color:var(--text)}
.feature h3{position:absolute;font-size:22px;font-weight:600}
.feature p{position:absolute;font-size:11.5px;line-height:18px;color:var(--text)}
.card{position:absolute;top:2306px;width:208px;height:296px;border:1px solid var(--card-line);background:#fff}
.bag{position:absolute;left:44px;top:50px;width:120px;height:196px;border-radius:6px}
.card-label{position:absolute;top:2620px;width:208px;text-align:center;font-size:14px;font-weight:500}
.impact{left:0;top:2785px;width:1200px;height:442px;background:var(--pink)}
.drops{left:0;top:3227px;width:1200px;height:647px;background:linear-gradient(180deg,#e23a2c 0%,#d5322a 100%)}
.drops-label{position:absolute;top:3710px;color:#fff;font-size:16px;font-weight:600;transform:translateX(-50%)}
.footer{left:0;top:4180px;width:1200px;height:473px;background:var(--footer);color:#fff}
.footer h4{position:absolute;top:166px;font-size:15px;font-weight:500}
.footer h4::after{content:"";display:block;width:52px;height:1px;background:#777;margin-top:8px}
.footer li{position:absolute;list-style:none;font-size:11.5px;color:#ddd;line-height:16px}
.social{position:absolute;top:210px;width:16px;height:16px;border:1.5px solid #fff;border-radius:50%}
.pay{position:absolute;top:4615px;width:29px;height:16px;border-radius:2px}
</style>
</head>
<body>

<div class="abs topbar">WELCOME TO VELMORA ROASTERS</div>

<header class="abs header">
  <div class="abs brand"><span class="brand-dot"></span>Velmora Roasters</div>
  <nav class="nav">
    <a style="left:390px">HOME</a>
    <a style="left:485px">ABOUT</a>
    <a style="left:584px">MERCH</a>
    <a style="left:687px">COFFEE</a>
    <a style="left:795px">VELMORAQ</a>
  </nav>
  <svg class="icon" style="left:926px" width="20" height="20" viewBox="0 0 20 20" fill="none" stroke="#222" stroke-width="1.8"><circle cx="8" cy="8" r="6"/><path d="M12.5 12.5L18 18"/></svg>
  <svg class="icon" style="left:972px" width="20" height="20" viewBox="0 0 20 20" fill="none" stroke="#222" stroke-width="1.8"><circle cx="10" cy="6" r="4"/><path d="M2 19c1-5 4-7 8-7s7 2 8 7"/></svg>
  <svg class="icon" style="left:1012px" width="22" height="20" viewBox="0 0 22 20" fill="none" stroke="#222" stroke-width="1.8"><path d="M2 5h16l-2 12H4z"/><path d="M7 5a3 3 0 016 0"/><circle cx="18" cy="3" r="3" fill="var(--red)" stroke="none"/></svg>
</header>

<section class="abs hero" role="img" aria-label="Roasted coffee beans and burlap sack in warm light">
  <h1 style="top:107px;font-size:58px">Crafted Coffee</h1>
  <h1 style="top:166px;font-size:74px">Cultured Identity</h1>
  <p>Single Origin Beans. Rare Blends. Designed Lifestyle.</p>
  <div class="btn" style="left:455px;top:290px;width:131px;height:36px">Shop Coffee</div>
  <div class="btn" style="left:593px;top:290px;width:151px;height:36px">Explore VelmoraQ</div>
</section>

<h2 class="section-title" style="top:612px">About Us</h2>
<p class="abs about-text">It is a long established fact that a reader will be distracted by the readable content of a page when looking at its layout. The point of using Lorem Ipsum is that it has a more-or-less normal distribution of letters, as opposed to using 'Content here, content here', making it look like readable English. Many desktop publishing packages and web page editors now use Lorem Ipsum as their default model text, and a search for 'lorem ipsum' will uncover many web sites still in their infancy.</p>
<div class="btn" style="left:533px;top:792px;width:136px;height:37px">Learn More</div>

<h2 class="section-title" style="top:880px">Explore VelmoraQ</h2>

<div class="bean-area" role="img" aria-label="Decorative scattered coffee beans along the left margin" style="left:0;top:795px;width:72px;height:450px"></div>
<div class="bean-area" role="img" aria-label="Decorative scattered coffee beans along the right margin" style="left:1128px;top:1270px;width:72px;height:450px"></div>

<div class="feature">
  <div class="photo" role="img" aria-label="Iced cold brew with cream in a tall glass" style="left:161px;top:978px;width:414px;height:357px;background:linear-gradient(135deg,#8c8a86,#3e3a36)"></div>
  <h3 style="left:623px;top:1044px">Cold Brew</h3>
  <p style="left:625px;top:1087px;width:410px">Grown in Puerto Rico's high mountains, our Arabica beans are cultivated with care and tradition. As coffee nerds would do, we decided to invite all our coffee nerd friends and the community of coffee enthusiasts to compete to see who could pour the best latte.<br><br>Add a few pints in with some great coffee and a DJ and you've got a good time.</p>
  <div class="btn" style="left:625px;top:1224px;width:113px;height:36px">See All</div>

  <div class="photo" role="img" aria-label="Coffee liqueur bottle beside a glass of creamy coffee" style="left:623px;top:1388px;width:414px;height:356px;background:linear-gradient(135deg,#6f5a3e,#2d241b)"></div>
  <h3 style="left:166px;top:1474px">Coffee Liquor</h3>
  <p style="left:166px;top:1518px;width:400px">Leave it to the experts. We'll surprise you with great coffee at your door step every time.<br><br>Always compostable packaging.</p>
  <div class="btn" style="left:166px;top:1616px;width:115px;height:36px">See All</div>

  <div class="photo" role="img" aria-label="Absinthe coffee in a champagne glass with falling sparkle" style="left:161px;top:1800px;width:414px;height:356px;background:radial-gradient(ellipse at 50% 60%,#5a3d28,#0f0c0a 70%)"></div>
  <h3 style="left:623px;top:1856px">Absinthe Coffee</h3>
  <p style="left:625px;top:1898px;width:415px">We're a North Wales coffee roaster with a mission to support cafes, shop owners, and baristas in pursuing the highest quality craft coffee. We're also a retail and craft coffee subscription provider bringing a unique and exciting coffee experience to our customers across the UK.<br><br>More importantly, we are social. We strive for opportunities to connect and serve our local community, our neighbours, and friends.</p>
  <div class="btn" style="left:625px;top:2058px;width:113px;height:35px">See All</div>
</div>

<h2 class="section-title" style="top:2224px">Our Collection</h2>
<div class="card" style="left:161px"><div class="bag" role="img" aria-label="Black single origin coffee bag" style="background:linear-gradient(180deg,#2a2a2a,#111)"></div></div>
<div class="card" style="left:385px"><div class="bag" role="img" aria-label="White and red Tamblin series coffee bag" style="background:linear-gradient(180deg,#f1f1f1,#d84c4c)"></div></div>
<div class="card" style="left:607px"><div class="bag" role="img" aria-label="Black and red Quillet series coffee bag" style="background:linear-gradient(180deg,#222,#9d1f1f)"></div></div>
<div class="card" style="left:829px"><div class="bag" role="img" aria-label="White and teal decaf coffee bag" style="background:linear-gradient(180deg,#f2f2f2,#bfdad8)"></div></div>
<div class="card-label" style="left:161px">Single Origin</div>
<div class="card-label" style="left:385px">Tamblin series</div>
<div class="card-label" style="left:607px">Quillet Series</div>
<div class="card-label" style="left:829px">Decaf</div>
<div class="btn" style="left:524px;top:2689px;width:152px;height:35px">View All Products</div>

<section class="abs impact">
  <h2 class="abs" style="left:161px;top:112px;font-size:37px;font-weight:700;line-height:38px">Your Coffee Makes<br>A Difference</h2>
  <p class="abs" style="left:161px;top:211px;width:420px;font-size:12.5px;line-height:18px;color:var(--text)">For every bag sold, we donate $1 to empower people with intellectual disabilities — supporting inclusion, independence, and opportunity through local and U.S. nonprofits.</p>
  <div class="btn" style="left:161px;top:285px;width:235px;height:35px">Learn More About Our Impact</div>
  <div class="photo" role="img" aria-label="Woman holding a coffee mug" style="left:667px;top:50px;width:146px;height:168px;background:linear-gradient(135deg,#b8a38f,#4f4038)"></div>
  <div class="photo" role="img" aria-label="Couple sharing coffee together" style="left:667px;top:233px;width:146px;height:166px;background:linear-gradient(135deg,#a48b74,#3a2f2a)"></div>
  <div class="photo" role="img" aria-label="Woman enjoying a cup of latte" style="left:835px;top:132px;width:177px;height:184px;background:linear-gradient(135deg,#c9a88e,#5b3a2c)"></div>
</section>

<section class="abs drops" role="img" aria-label="Red backdrop with silhouette of a samurai and trees">
  <h2 class="abs" style="left:0;top:48px;width:1200px;text-align:center;color:#fff;font-size:32px;font-weight:600">Limited Drops No Restocks</h2>
  <div class="abs" style="left:381px;top:198px;width:1px;height:282px;background:rgba(255,255,255,.5)"></div>
  <div class="abs" style="left:829px;top:198px;width:1px;height:282px;background:rgba(255,255,255,.5)"></div>
  <div class="photo" role="img" aria-label="Black branded t-shirt" style="left:43px;top:158px;width:289px;height:296px;background:linear-gradient(180deg,#1c1c1c,#0e0e0e)"></div>
  <div class="photo" role="img" aria-label="Black branded cap" style="left:464px;top:197px;width:259px;height:244px;background:linear-gradient(180deg,#1c1c1c,#0e0e0e)"></div>
  <div class="photo" role="img" aria-label="Black branded mug" style="left:889px;top:194px;width:268px;height:256px;background:linear-gradient(180deg,#1c1c1c,#0e0e0e)"></div>
</section>
<div class="drops-label" style="left:188px">Tshirts</div>
<div class="drops-label" style="left:593px">Hats</div>
<div class="drops-label" style="left:1023px">Mugs</div>
<div class="btn" style="left:511px;top:3784px;width:177px;height:36px;background:#fff;color:#222">View All Products</div>

<h2 class="abs" style="left:0;top:3950px;width:1200px;text-align:center;font-size:37px;font-weight:300;line-height:46px">We Don't Just Sell Coffee.<br><span style="font-weight:600">We Build Rituals.</span></h2>
<div class="btn" style="left:524px;top:4075px;width:152px;height:36px">Shop Now</div>

<footer class="abs footer">
  <div class="abs" style="left:164px;top:40px;font-size:15px;font-weight:500">SIGN UP FOR OUR NEWSLETTER</div>
  <div class="abs" style="left:164px;top:60px;font-size:11px;color:#ccc">Give your inbox some love with new products tips, &amp; more.</div>
  <div class="abs" style="left:604px;top:36px;width:336px;height:40px;background:#fff;color:#888;font-size:11px;padding:12px 12px">Enter Email Address</div>
  <div class="btn" style="left:940px;top:36px;width:101px;height:40px;font-size:11px;font-weight:600">SUBSCRIBE</div>
  <div class="abs" style="left:161px;top:110px;width:880px;height:1px;background:#444"></div>

  <h4 style="left:161px">Quick Links</h4>
  <ul>
    <li style="left:161px;top:213px">About</li>
    <li style="left:161px;top:251px">Merch</li>
    <li style="left:161px;top:289px">Coffee</li>
    <li style="left:161px;top:327px">VelmoraQ</li>
  </ul>
  <h4 style="left:349px">Support</h4>
  <ul>
    <li style="left:349px;top:213px">FAQs</li>
    <li style="left:349px;top:251px">Contact Us:<br>support@velmoraroasters.com</li>
    <li style="left:349px;top:300px">Phone: (555) 014-2279</li>
  </ul>
  <h4 style="left:576px">Latest News</h4>
  <ul>
    <li style="left:576px;top:213px">The Best Tungsten and Titanium Rings - Full Guide</li>
    <li style="left:576px;top:251px">How is Tungsten or Titanium Ring Size Measured?</li>
    <li style="left:576px;top:289px;width:280px">Black, Silver Gold - The best colors for mens tungsten and titanium rings</li>
    <li style="left:576px;top:340px">Whats better tungsten or titanium for a mens ring</li>
  </ul>
  <h4 style="left:938px">Connect</h4>
  <span class="social" style="left:936px"></span>
  <span class="social" style="left:979px"></span>
  <span class="social" style="left:1022px"></span>
</footer>

<span class="pay" style="left:430px;background:#2a6ebb"></span>
<span class="pay" style="left:464px;background:#fff"></span>
<span class="pay" style="left:498px;background:#3b5ba8"></span>
<span class="pay" style="left:532px;background:#fff"></span>
<span class="pay" style="left:566px;background:#fff"></span>
<span class="pay" style="left:600px;background:#ea6a3a"></span>
<span class="pay" style="left:634px;background:#253b80"></span>
<span class="pay" style="left:668px;background:#6b3fd1"></span>
<span class="pay" style="left:702px;background:#3aa0d8"></span>
<span class="pay" style="left:736px;background:#fff"></span>

</body>
</html>
```